Book Cover

Book cover for a study guide on Galatians. The title would be: "Unbound Hearts: Called Out to Walk Open" Possibly using a bird breaking free from a cage.+

Target Market(s)

We will sell them to our church.

Requirements
Must have
• Authors are Dr. Martin Oskerby and Dr. Helen Oskerby

```html
<!DOCTYPE html>
<html lang="en">
<head>
<meta charset="utf-8">
<title>Unbound Hearts – Book Cover</title>
<link href="https://fonts.googleapis.com/css2?family=Barlow:wght@500&family=Libre+Baskerville&family=Playfair+Display:wght@400&family=Tinos&display=swap" rel="stylesheet">
<style>
  :root {
    --page: #ffffff;
    --paper: #f5f5f5;
    --navy: #123a78;
    --ink: #1f2330;
    --red: #e8331f;
    --text: #222222;
    --chain-light: #d9d9d9;
    --chain-dark: #3a3a3a;
  }
  html, body {
    margin: 0;
    width: 1200px;
    height: 1200px;
    overflow: hidden;
    background: var(--page);
  }
  .canvas {
    position: relative;
    width: 1200px;
    height: 1200px;
  }
  .spread {
    position: absolute;
    left: 40px;
    top: 218px;
    width: 1121px;
    height: 821px;
    background: var(--paper);
    overflow: hidden;
  }
  /* Back cover */
  .back-art {
    position: absolute;
    left: 0;
    top: 0;
    width: 143px;
    height: 821px;
    background: linear-gradient(180deg, var(--chain-light) 0%, #8a8a8a 30%, var(--paper) 45%, #9a9a9a 65%, var(--chain-dark) 85%, #bdbdbd 100%);
  }
  .back-title {
    position: absolute;
    right: 609px;
    top: 50px;
    margin: 0;
    text-align: right;
    font-family: "Playfair Display", serif;
    font-weight: 400;
    font-size: 48px;
    line-height: 1;
    color: var(--navy);
    white-space: nowrap;
  }
  .tagline {
    font-family: "Barlow", sans-serif;
    font-weight: 500;
    letter-spacing: 0.09em;
    color: var(--ink);
    white-space: nowrap;
  }
  .tagline .accent { color: var(--red); }
  .back-tagline {
    position: absolute;
    right: 609px;
    top: 150px;
    margin: 0;
    font-size: 20px;
    line-height: 1;
  }
  .blurb {
    position: absolute;
    right: 609px;
    top: 190px;
    width: 345px;
    margin: 0;
    text-align: right;
    font-family: "Tinos", serif;
    font-size: 13.4px;
    line-height: 18.5px;
    color: var(--text);
  }
  .blurb p { margin: 0 0 18.5px; }
  /* Spine */
  .spine {
    position: absolute;
    left: 539px;
    top: 0;
    width: 42px;
    height: 821px;
  }
  .spine-title, .spine-authors {
    position: absolute;
    left: 50%;
    margin: 0;
    writing-mode: vertical-rl;
    transform: translateX(-50%);
    font-family: "Tinos", serif;
    white-space: nowrap;
    font-size: 17px;
    line-height: 1;
  }
  .spine-title {
    top: 99px;
    color: var(--navy);
  }
  .spine-mark {
    position: absolute;
    left: 15px;
    top: 286px;
    width: 12px;
    height: 11px;
    background: var(--red);
  }
  .spine-authors {
    top: 415px;
    letter-spacing: 0.03em;
    color: var(--ink);
  }
  /* Front cover */
  .front {
    position: absolute;
    left: 582px;
    top: 0;
    width: 539px;
    height: 821px;
  }
  .thread {
    position: absolute;
    left: 263px;
    top: 0;
    width: 1.5px;
    height: 291px;
    background: var(--navy);
  }
  .front-tagline {
    position: absolute;
    right: 42px;
    top: 188px;
    margin: 0;
    text-align: right;
    font-size: 26px;
    line-height: 31px;
  }
  .cage-art {
    position: absolute;
    left: 195px;
    top: 291px;
    width: 138px;
    height: 239px;
    background: linear-gradient(180deg, #6f8bbd 0%, var(--navy) 100%);
    opacity: 0.85;
  }
  .bird-art {
    position: absolute;
    left: 370px;
    top: 352px;
    width: 77px;
    height: 77px;
    background: var(--red);
  }
  .front-title {
    position: absolute;
    left: 0;
    width: 539px;
    top: 542px;
    margin: 0;
    text-align: center;
    font-family: "Playfair Display", serif;
    font-weight: 400;
    font-size: 62px;
    line-height: 1;
    color: var(--navy);
    white-space: nowrap;
  }
  .front-authors {
    position: absolute;
    left: 0;
    width: 539px;
    top: 690px;
    margin: 0;
    text-align: center;
    font-family: "Libre Baskerville", serif;
    font-size: 32px;
    line-height: 46px;
    letter-spacing: 0.03em;
    color: var(--ink);
  }
</style>
</head>
<body>
<div class="canvas">
  <div class="spread">
    <section class="back-cover">
      <div class="back-art" role="img" aria-label="Grayscale illustration of hands breaking apart a heavy chain"></div>
      <h2 class="back-title">Unbound Hearts</h2>
      <p class="tagline back-tagline">CALLED OUT TO <span class="accent">WALK OPEN</span></p>
      <div class="blurb">
        <p>Contrary to popular belief, Lorem Ipsum is not simply random text. It has roots in a piece of classical Latin literature from 45 BC, making it over 2000 years old. Edwin Harrowgate, a Latin professor at Aldermoor College in Vermont, looked up one of the more obscure Latin words, consectetur, from a Lorem Ipsum passage, and going through the cites of the word in classical literature, discovered the undoubtable source. Lorem Ipsum comes from sections 1.10.32 and 1.10.33 of "de Finibus Bonorum et Malorum" (The Extremes of Good and Evil) by Marcus Tellan, written in 45 BC. This book is a treatise on the theory of ethics, very popular during the Renaissance. The first line of Lorem Ipsum, "Lorem ipsum dolor sit amet..", comes from a line in section 1.10.32.</p>
        <p>The standard chunk of Lorem Ipsum used since the 1500s is reproduced below for those interested. Sections 1.10.32 and 1.10.33 from "de Finibus Bonorum et Malorum" by Marcus Tellan are also reproduced in their exact original form, accompanied by English versions from the 1914 translation by J. Penwarden.</p>
      </div>
    </section>

    <section class="spine">
      <p class="spine-title">Unbound Hearts</p>
      <div class="spine-mark" role="img" aria-label="Small red origami bird"></div>
      <p class="spine-authors">Dr. Martin Oskerby &amp; Dr. Helen Oskerby</p>
    </section>

    <section class="front">
      <div class="thread"></div>
      <p class="tagline front-tagline">CALLED OUT TO<br><span class="accent">WALK OPEN</span></p>
      <div class="cage-art" role="img" aria-label="Navy line drawing of a hanging birdcage with its side broken open"></div>
      <div class="bird-art" role="img" aria-label="Red origami bird flying out of the cage"></div>
      <h1 class="front-title">Unbound Hearts</h1>
      <p class="front-authors">Dr. Martin Oskerby &amp;<br>Dr. Helen Oskerby</p>
    </section>
  </div>
</div>
</body>
</html>
```